Design Labels and Brand Look For Mens Soap Company

We are developing a mens soap line for a natural body wash and exfoliating bar. We will be selling this with our line of mens toiletry bags that we sell under the name of Corvane Totes on Quillmart. We are looking for you to design the product brand look with brand color palette and fonts.

The title for the mens body was is "Body Wash For Men". The title for the soap bar is "Exfoliating Bar Soap For Men"

We are providing the templates for these 2 items in PDF form. The final version of the design needs to be in a layered PSD format. You also need to send us the fonts used.

This soap will be sold on Quillmart. Do a search for "men's body wash" and "mens soap bar" you will see our competition on page one. We need to stand out with colors and design differentiaon.

Target Market(s)

Men

Industry/Entity Type

Skin Care Product

Requirements
Must have
• Layered PSD file with all fonts

```html
<!DOCTYPE html>
<html lang="en">
<head>
<meta charset="utf-8">
<title>Corvane — Body Wash For Men Label</title>
<link href="https://fonts.googleapis.com/css2?family=Oswald:wght@500;600&family=Lexend:wght@400&display=swap" rel="stylesheet">
<style>
  :root {
    --page-bg: #ffffff;
    --label-blue: #3a3a9c;
    --label-white: #f4f4f8;
    --accent-orange: #e2561e;
    --muted-lavender: #c6c5ec;
  }
  html, body {
    margin: 0;
    padding: 0;
    width: 1008px;
    height: 1200px;
    overflow: hidden;
    background: var(--page-bg);
  }
  .label {
    position: absolute;
    left: 124px;
    top: 170px;
    width: 760px;
    height: 861px;
    background: var(--label-blue);
    color: var(--label-white);
  }
  .brand-name {
    position: absolute;
    left: 0;
    right: 0;
    top: 92px;
    text-align: center;
    font-family: "Oswald", sans-serif;
    font-weight: 600;
    font-size: 64px;
    line-height: 1;
    letter-spacing: 1px;
    color: var(--label-white);
  }
  .product-title {
    position: absolute;
    left: 168px;
    top: 188px;
    margin: 0;
    font-family: "Oswald", sans-serif;
    font-weight: 600;
    text-transform: uppercase;
    color: var(--label-white);
  }
  .product-title .title-line {
    display: block;
    font-size: 152px;
    line-height: 152px;
    letter-spacing: 1px;
  }
  .product-title .title-sub {
    display: block;
    font-size: 64px;
    line-height: 64px;
    margin-top: 8px;
    letter-spacing: 0.5px;
  }
  .feature-tag {
    position: absolute;
    left: 168px;
    top: 636px;
    width: 332px;
    height: 45px;
    background: var(--accent-orange);
    box-sizing: border-box;
    padding-left: 14px;
    font-family: "Lexend", sans-serif;
    font-size: 24px;
    line-height: 45px;
    letter-spacing: 1px;
    color: var(--label-white);
    text-transform: uppercase;
  }
  .feature-list {
    position: absolute;
    left: 168px;
    top: 698px;
    margin: 0;
    padding: 0;
    list-style: none;
    font-family: "Lexend", sans-serif;
    font-size: 22px;
    line-height: 27px;
    letter-spacing: 1.5px;
    text-transform: uppercase;
    color: var(--muted-lavender);
  }
  .net-volume {
    position: absolute;
    left: 168px;
    top: 800px;
    margin: 0;
    font-family: "Lexend", sans-serif;
    font-size: 22px;
    letter-spacing: 1.5px;
    text-transform: uppercase;
    color: var(--muted-lavender);
  }
</style>
</head>
<body>
  <main class="label">
    <div class="brand-name">Corvane</div>
    <h1 class="product-title">
      <span class="title-line">Body</span>
      <span class="title-line">Wash</span>
      <span class="title-sub">For Men</span>
    </h1>
    <div class="feature-tag">Loremp Ipsum</div>
    <ul class="feature-list">
      <li>Natural Ingredients</li>
      <li>Moisturizing</li>
    </ul>
    <p class="net-volume">16 FL OZ (473 ML)</p>
  </main>
</body>
</html>
```